Payday Lending App Interface Design

Hello, we are building a payday lending application, Lendora, that lend people money. I have drafted some of the screens that show the functionalities we have at the moment, please find the screens in attachments.
The elements in the screens are placed just to show what should be included in those screens, it's not necessary to follow the same layout. If you have better design ideas, you are very welcomed to show off your talent.
I think what we want is a style guide so that we can apply the same style to any screens that are similar to the ones I attached. We really like
the style as in the attached image called Style.png. We might want something similar - a simple, clean design yet fun and engaging. Customised graphical elements such as icons, illustrations are preferable.
Apart from the attached screens, we might also need a design for the On Board screen and the Login/Sign Up screen too.
Our logo colour is in yellow and black. Perhaps we will have a similar colour theme. I also attached the logo file, icon-Lendora.png, if you would like to put it in your design.
Please message me if you need further information.
Regards
Target Market(s)
Young people that doesn't have strong income
Look and feel

```html
<!DOCTYPE html>
<html lang="en">
<head>
<meta charset="utf-8">
<title>Lendora – Revised UI Screens</title>
<link href="https://fonts.googleapis.com/css2?family=Outfit:wght@400;500;700;800&family=Poppins:wght@400;500;600;700&family=Mulish:wght@400;600;800&display=swap" rel="stylesheet">
<style>
:root{
  --ink:#111111;
  --night:#1c1c1e;
  --night-2:#2b2b2e;
  --yellow:#ffc107;
  --yellow-text:#f5b800;
  --card:#f4f4f5;
  --muted:#6b6b6b;
  --faint:#a8a8a8;
  --line:#e6e6e6;
  --green:#3bb54a;
  --red:#e53935;
  --grey-dot:#a3a3a3;
  --panel:#efefef;
  --frame:#3a3a3c;
  --body:#2c3140;
}
*{box-sizing:border-box;margin:0;padding:0}
html,body{width:1200px;height:1093px;overflow:hidden;background:#fff}
body{position:relative;font-family:"Outfit",sans-serif;color:var(--ink)}
.abs{position:absolute}
.board-title{left:0;width:1200px;top:44px;text-align:center;font-size:39px;font-weight:800;letter-spacing:.2px}
.section-title{top:128px;font-size:29px;font-weight:800;transform:translateX(-50%);white-space:nowrap}

/* phones */
.phone{position:absolute;border:5px solid var(--ink);border-radius:24px;overflow:hidden;background:#fff;font-family:"Poppins",sans-serif}
.phone .abs{position:absolute}
.status{top:12px;left:19px;right:19px;display:flex;justify-content:space-between;font-size:8px;font-weight:600}
.status svg{width:36px;height:8px}
.screen-title{left:0;right:0;top:36px;text-align:center;font-size:12.5px;font-weight:500}
.back{left:16px;top:39px;width:8px;height:12px}
.dark{color:#fff}

/* choose loan */
.choose-hero{left:0;top:0;right:0;height:172px;background:linear-gradient(180deg,#141416,#26262a);border-radius:0 0 10px 10px}
.amount-label{left:0;right:0;top:70px;text-align:center;font-size:8px;font-weight:500;color:var(--yellow-text)}
.amount{left:0;right:0;top:89px;text-align:center;font-size:20px;font-weight:700;color:#fff}
.amount-arrow{top:97px;width:6px;height:10px}
.max-pill{left:69px;top:119px;width:83px;height:13px;border-radius:7px;background:#3d3d40;color:var(--yellow-text);font-size:6px;text-align:center;line-height:13px}
.fee-card{left:14px;top:150px;width:186px;height:36px;background:#fff;border-radius:4px 4px 0 0;display:flex;justify-content:space-around;align-items:center;text-align:center;font-size:6px;line-height:1.5}
.fee-card b{font-weight:600;font-size:7px}
.installment-band{left:14px;top:186px;width:186px;height:33px;background:var(--ink);border-radius:0 0 4px 4px;color:#fff;font-size:7.5px;text-align:center;line-height:33px}
.cycle-card{left:14px;top:240px;width:186px;height:45px;background:#fff;border-radius:5px;box-shadow:0 1px 6px rgba(0,0,0,.08)}
.icon-tile{width:30px;height:30px;border-radius:6px;background:var(--card);display:flex;align-items:center;justify-content:center}
.icon-tile svg{width:14px;height:14px}
.cycle-card .icon-tile{position:absolute;left:8px;top:7px}
.cycle-card .main{position:absolute;left:47px;top:9px;font-size:9px;font-weight:500}
.cycle-card .sub{position:absolute;left:47px;top:25px;font-size:7px;color:var(--muted)}
.cycle-card .chev{position:absolute;right:9px;top:16px;width:13px;height:13px}
.term-label{left:14px;top:304px;font-size:7.5px;font-weight:500}
.slider-card{left:14px;top:315px;width:186px;height:45px;background:#fff;border-radius:5px;box-shadow:0 1px 6px rgba(0,0,0,.07)}
.slider-card .lo{position:absolute;left:10px;top:9px;font-size:6px}
.slider-card .hi{position:absolute;right:10px;top:9px;font-size:6px}
.track{position:absolute;left:11px;right:11px;top:29px;height:2px;background:var(--ink)}
.track i{position:absolute;left:0;top:0;height:2px;width:86px;background:var(--yellow)}
.knob{position:absolute;left:91px;top:22px;width:16px;height:16px;border-radius:50%;background:var(--yellow);font-size:7px;font-weight:600;text-align:center;line-height:16px}
.btn-yellow{background:var(--yellow);border-radius:5px;text-align:center;font-size:8px;font-weight:600;color:var(--ink)}

/* home */
.home-hero{left:0;right:0;top:0;height:116px;background:linear-gradient(180deg,#121214,#2a2a2e);border-radius:0 0 12px 12px}
.home-hero .hello{left:21px;top:77px;font-size:10px;line-height:15px;color:#fff}
.home-hero .hello b{font-weight:600}
.hero-art{left:114px;top:66px;width:76px;height:50px;border-radius:26px 6px 0 0;background:linear-gradient(135deg,#5a5a60,#2e2e33 60%,#f0b400)}
.menu{left:13px;top:40px;width:18px;height:13px}
.bell{left:171px;top:38px;width:14px;height:14px}
.gear{left:192px;top:38px;width:14px;height:14px}
.timeline{left:23px;top:155px;height:345px;border-left:1.2px dashed #555}
.step-dot{width:19px;height:19px;border-radius:50%;display:flex;align-items:center;justify-content:center}
.step-dot svg{width:10px;height:10px}
.step-card{left:45px;width:155px;background:#fff;border-radius:6px;box-shadow:0 1px 7px rgba(0,0,0,.08);padding:8px 12px}
.step-card h4{font-size:8.5px;font-weight:600;margin-bottom:4px}
.step-card p{font-size:7px;line-height:12px;color:var(--muted)}
.step-card.alert h4{color:var(--red)}
.step-card.current h4{color:var(--yellow-text)}
.step-card.locked h4,.step-card.locked p{color:var(--faint)}

/* summary */
.info-card{left:13px;width:186px;height:45px;background:var(--card);border-radius:6px}
.info-card .icon-tile{position:absolute;left:10px;top:8px;background:#ebebec}
.info-card .k{position:absolute;left:49px;top:9px;font-size:8.5px;font-weight:500}
.info-card .v{position:absolute;left:49px;top:25px;font-size:7px;color:var(--muted)}
.agreement{left:13px;top:307px;width:186px;height:187px;background:#fff;border-radius:6px;box-shadow:0 1px 7px rgba(0,0,0,.07);padding:10px 8px;font-size:5.8px;line-height:10.3px;color:#444;text-align:justify}
.agreement h5{font-size:7.5px;font-weight:600;color:var(--ink);line-height:12px}
.agreement b{font-weight:600;color:var(--ink);display:block}

/* wireframe */
.wire-panel{left:913px;top:184px;width:246px;height:492px;background:var(--panel);font-family:"Mulish",sans-serif}
.wire-panel .label{left:16px;top:8px;font-size:17px;color:#8a8a8a}
.wire-phone{left:15px;top:38px;width:216px;height:445px;border:10px solid var(--frame);border-radius:34px;background:#fff}
.notch{left:42px;top:-10px;width:112px;height:18px;background:var(--frame);border-radius:0 0 12px 12px}
.wire-title{left:0;right:0;top:66px;text-align:center;font-size:13px;font-weight:800;line-height:18px}
.logo-box{left:69px;top:105px;width:49px;height:46px;border:1.3px solid #222;border-radius:6px;font-size:14px;text-align:center;line-height:44px}
.wire-field{left:17px;font-size:13px}
.wire-field.k{font-weight:800}
.wire-btn{left:15px;top:381px;width:156px;height:24px;background:#1f1f1f;color:#fff;font-size:8.5px;text-align:center;line-height:24px}

/* notes */
.note{font-size:21px;line-height:28px;color:var(--body)}
.note h3{font-size:22px;font-weight:800;color:var(--ink);line-height:27px}
.note ul{margin-left:34px;margin-top:14px}
.note li{padding-left:4px}
.note .quote{font-style:italic;font-weight:700;color:var(--body)}
</style>
</head>
<body>

<div class="abs board-title">Revised UI Screen</div>
<div class="abs section-title" style="left:167px">Choose Loan</div>
<div class="abs section-title" style="left:477px">Homescreen</div>
<div class="abs section-title" style="left:754px">Loan Summary</div>

<!-- Choose Loan screen -->
<div class="phone" style="left:56px;top:180px;width:224px;height:473px">
  <div class="abs choose-hero"></div>
  <div class="abs status dark"><span>9:41</span><svg viewBox="0 0 36 8"><rect x="0" y="5" width="2" height="3" fill="#fff"/><rect x="3" y="3.5" width="2" height="4.5" fill="#fff"/><rect x="6" y="2" width="2" height="6" fill="#fff"/><path d="M13 3.5a5 5 0 0 1 7 0M14.5 5a3 3 0 0 1 4 0" stroke="#fff" fill="none" stroke-width="1"/><circle cx="16.5" cy="7" r=".9" fill="#fff"/><rect x="24" y="1.5" width="10" height="5" rx="1" fill="#fff"/></svg></div>
  <svg class="abs back" viewBox="0 0 8 12"><path d="M6 1 1.5 6 6 11" stroke="#fff" stroke-width="1.6" fill="none"/></svg>
  <div class="abs screen-title dark">Choose Loan</div>
  <div class="abs amount-label">Choose Amount</div>
  <svg class="abs amount-arrow" style="left:60px" viewBox="0 0 6 10"><path d="M5 1 1 5l4 4" stroke="#fff" stroke-width="1.5" fill="none"/></svg>
  <div class="abs amount">$ 2,500</div>
  <svg class="abs amount-arrow" style="left:158px" viewBox="0 0 6 10"><path d="M1 1l4 4-4 4" stroke="#fff" stroke-width="1.5" fill="none"/></svg>
  <div class="abs max-pill">Max $ 5,000</div>
  <div class="abs fee-card"><div>Installment Fee (12%)<br><b>6 x $ 24.99</b></div><div>Admin Fee (0.5%)<br><b>$ 12.5</b></div></div>
  <div class="abs installment-band">Installment 6 Months x $ 233.32</div>
  <div class="abs cycle-card">
    <div class="icon-tile"><svg viewBox="0 0 14 14"><rect x="1" y="2.5" width="12" height="10.5" rx="1.5" fill="#111"/><rect x="3" y="1" width="1.5" height="3" fill="#111"/><rect x="9.5" y="1" width="1.5" height="3" fill="#111"/><rect x="1" y="5" width="12" height=".8" fill="#fff"/></svg></div>
    <div class="main">Fortnightly (2 Weeks)</div>
    <div class="sub">Choose Repayment Cycle</div>
    <svg class="chev" viewBox="0 0 13 13"><circle cx="6.5" cy="6.5" r="5.7" stroke="#111" fill="none" stroke-width="1"/><path d="M4 5.5l2.5 2.5L9 5.5" stroke="#111" fill="none" stroke-width="1"/></svg>
  </div>
  <div class="abs term-label">Loan Term</div>
  <div class="abs slider-card">
    <span class="lo">1 Month</span><span class="hi">12 Month</span>
    <div class="track"><i></i></div>
    <div class="knob">6</div>
  </div>
  <div class="abs btn-yellow" style="left:14px;top:406px;width:186px;height:34px;line-height:34px">Next</div>
</div>

<!-- Homescreen -->
<div class="phone" style="left:365px;top:180px;width:224px;height:552px">
  <div class="abs home-hero"></div>
  <div class="abs status dark"><span>9:41</span><svg viewBox="0 0 36 8"><rect x="0" y="5" width="2" height="3" fill="#fff"/><rect x="3" y="3.5" width="2" height="4.5" fill="#fff"/><rect x="6" y="2" width="2" height="6" fill="#fff"/><path d="M13 3.5a5 5 0 0 1 7 0M14.5 5a3 3 0 0 1 4 0" stroke="#fff" fill="none" stroke-width="1"/><circle cx="16.5" cy="7" r=".9" fill="#fff"/><rect x="24" y="1.5" width="10" height="5" rx="1" fill="#fff"/></svg></div>
  <svg class="abs menu" viewBox="0 0 18 13"><path d="M0 1.5h18M0 6.5h18M0 11.5h18" stroke="#fff" stroke-width="1.8"/></svg>
  <div class="abs screen-title dark">Welcome</div>
  <svg class="abs bell" viewBox="0 0 14 14"><path d="M3 10V6.5a4 4 0 0 1 8 0V10l1 1.2H2z" fill="#fff"/><circle cx="7" cy="12.5" r="1.2" fill="#fff"/><circle cx="11" cy="3" r="2.6" fill="var(--yellow)"/></svg>
  <svg class="abs gear" viewBox="0 0 14 14"><circle cx="7" cy="7" r="5.5" stroke="#fff" fill="none" stroke-width="1.3" stroke-dasharray="2.2 1.1"/><circle cx="7" cy="7" r="2" stroke="#fff" fill="none" stroke-width="1.2"/></svg>
  <div class="abs hello" style="left:21px;top:77px;font-size:10px;line-height:15px;color:#fff">Hello,<br><b style="font-weight:600">Mara Lind</b></div>
  <div class="abs hero-art" role="img" aria-label="Illustration of a person tossing coins"></div>

  <div class="abs timeline"></div>
  <div class="abs step-dot" style="left:14px;top:160px;background:var(--green)"><svg viewBox="0 0 10 10"><path d="M2 5.2l2 2 4-4.4" stroke="#fff" stroke-width="1.6" fill="none"/></svg></div>
  <div class="abs step-dot" style="left:14px;top:235px;background:var(--red)"><svg viewBox="0 0 10 10"><path d="M2.5 2.5l5 5M7.5 2.5l-5 5" stroke="#fff" stroke-width="1.5"/></svg></div>
  <div class="abs step-dot" style="left:14px;top:304px;background:var(--green)"><svg viewBox="0 0 10 10"><path d="M2 5.2l2 2 4-4.4" stroke="#fff" stroke-width="1.6" fill="none"/></svg></div>
  <div class="abs step-dot" style="left:14px;top:361px;background:var(--yellow)"><svg viewBox="0 0 10 10"><path d="M5 1.5v4.5" stroke="#fff" stroke-width="1.6"/><circle cx="5" cy="8" r=".9" fill="#fff"/></svg></div>
  <div class="abs step-dot" style="left:14px;top:427px;background:var(--grey-dot)"></div>
  <div class="abs step-dot" style="left:14px;top:491px;background:var(--grey-dot)"></div>

  <div class="abs step-card" style="top:141px;height:55px"><h4>Get Started</h4><p>What you need to know before applying a loan</p></div>
  <div class="abs step-card alert" style="top:213px;height:65px"><h4>Basic Information</h4><p>Your ID document are expired. Upload your document again to get qualified</p></div>
  <div class="abs step-card" style="top:293px;height:39px"><h4>Connect Bank Account</h4><p>Add your own bank account</p></div>
  <div class="abs step-card current" style="top:348px;height:45px"><h4>Apply a Loan</h4><p>Get a loan that fit to your needs</p></div>
  <div class="abs step-card locked" style="top:408px;height:56px"><h4>Repayments</h4><p>Pay your installments before due date!</p></div>
  <div class="abs step-card locked" style="top:479px;height:43px"><h4>Loan Closed</h4><p>Thank you for using Lendora</p></div>
</div>

<!-- Loan Summary -->
<div class="phone" style="left:643px;top:180px;width:224px;height:570px">
  <div class="abs status"><span>9:41</span><svg viewBox="0 0 36 8"><rect x="0" y="5" width="2" height="3" fill="#111"/><rect x="3" y="3.5" width="2" height="4.5" fill="#111"/><rect x="6" y="2" width="2" height="6" fill="#111"/><path d="M13 3.5a5 5 0 0 1 7 0M14.5 5a3 3 0 0 1 4 0" stroke="#111" fill="none" stroke-width="1"/><circle cx="16.5" cy="7" r=".9" fill="#111"/><rect x="24" y="1.5" width="10" height="5" rx="1" fill="#111"/></svg></div>
  <svg class="abs back" viewBox="0 0 8 12"><path d="M6 1 1.5 6 6 11" stroke="#111" stroke-width="1.6" fill="none"/></svg>
  <div class="abs screen-title">Loan Summary</div>

  <div class="abs info-card" style="top:66px"><div class="icon-tile"><svg viewBox="0 0 14 14"><circle cx="7" cy="4.5" r="3" fill="#111"/><path d="M1.5 13a5.5 5 0 0 1 11 0z" fill="#111"/></svg></div><div class="k">Application Name</div><div class="v">Mara Lind</div></div>
  <div class="abs info-card" style="top:127px"><div class="icon-tile"><svg viewBox="0 0 14 14"><path d="M5 1h4L8 3.5H6z" fill="#111"/><path d="M7 3.5c-4 0-5.5 4-5.5 6.5 0 2 1.5 3 5.5 3s5.5-1 5.5-3c0-2.5-1.5-6.5-5.5-6.5z" fill="#111"/><text x="7" y="11" font-size="6" fill="#fff" text-anchor="middle" font-family="Poppins,sans-serif">$</text></svg></div><div class="k">Loan Amount</div><div class="v">$ 2,500</div></div>
  <div class="abs info-card" style="top:187px"><div class="icon-tile"><svg viewBox="0 0 14 14"><rect x="1" y="2.5" width="12" height="10.5" rx="1.5" fill="#111"/><rect x="3" y="1" width="1.5" height="3" fill="#111"/><rect x="9.5" y="1" width="1.5" height="3" fill="#111"/><rect x="1" y="5" width="12" height=".8" fill="#fff"/></svg></div><div class="k">Repayment Cycle</div><div class="v">Fortnightly</div></div>
  <div class="abs info-card" style="top:248px"><div class="icon-tile"><svg viewBox="0 0 14 14"><path d="M3 1h6l3 3v9H3z" fill="none" stroke="#111" stroke-width="1.2"/><path d="M5 6h5M5 8.5h5M5 11h3" stroke="#111" stroke-width="1"/></svg></div><div class="k">Loan Term</div><div class="v">6 Months</div></div>

  <div class="abs agreement">
    <h5>Loan Agreement</h5>
    <b>Lorem Ipsum</b>
    Lorem ipsum dolor sit amet, consectetur adipiscing elit, sed do eiusmod tempor incididunt ut labore et dolore magna aliqua. Integer enim neque volutpat ac. Mi quis hendrerit dolor magna eget est lorem ipsum dolor. Aenean vel elit scelerisque mauris pellentesque pulvinar pellentesque habitant.
    <b>Lorem Ipsum</b>
    Massa tincidunt dui ut ornare lectus sit amet est. Et egestas quis ipsum suspendisse ultrices gravida dictum fusce ut. Pulvinar neque laoreet suspendisse interdum consectetur. Sodales ut etiam sit amet nisl purus. Dui faucibus in ornare quam.
  </div>
  <div class="abs btn-yellow" style="left:13px;top:509px;width:186px;height:34px;line-height:34px">Confirm and Agree</div>
</div>

<!-- Wireframe reference -->
<div class="abs wire-panel">
  <div class="abs label">Loan Summary</div>
  <div class="abs wire-phone">
    <div class="abs notch"></div>
    <svg class="abs" style="left:21px;top:35px;width:11px;height:16px" viewBox="0 0 11 16"><path d="M9 1.5 2.5 8 9 14.5" stroke="#111" stroke-width="2.4" fill="none"/></svg>
    <div class="abs wire-title">Loan Summary and<br>agreement</div>
    <div class="abs logo-box">Logo</div>
    <div class="abs wire-field k" style="top:148px">Application name:</div>
    <div class="abs wire-field" style="top:169px">user full name</div>
    <div class="abs wire-field k" style="top:193px">Loan Amount:</div>
    <div class="abs wire-field" style="top:213px">$ XXXX</div>
    <div class="abs wire-field k" style="top:236px">Repayment Cycle:</div>
    <div class="abs wire-field" style="top:258px">Fortnightly</div>
    <div class="abs wire-field k" style="top:281px;left:18px">Loan term:</div>
    <div class="abs wire-field" style="top:302px;left:18px">6 months</div>
    <div class="abs wire-field" style="top:330px;left:18px">Agreement....Long text</div>
    <div class="abs wire-btn">Confirm and Agree</div>
  </div>
</div>

<!-- Notes -->
<div class="abs note" style="left:61px;top:692px;width:260px">
  <h3>Revised</h3>
  Slider shown Min -<br>Max loan term
</div>
<div class="abs note" style="left:370px;top:764px;width:230px">
  <h3>Revised</h3>
  Revised according to suggestions
  <ul><li>Added Illustrations</li><li>Changed card design</li></ul>
</div>
<div class="abs note" style="left:647px;top:764px;width:520px">
  <h3>Revised</h3>
  <div class="quote">“I think should look like a report which include the loan product the customer selected”</div>
  I'm a bit stuck here because I don't understand what content should be in the "Loan Product" because I refers to the existing wireframe. Are you referring to "Loan Product" as "Loan Amount"?
  <div style="margin-top:14px">Changed the Card design to make it look like a form that wasn't clickable, as before it was like something you could click on for further action</div>
</div>

</body>
</html>
```